Local Healthy meal delivery service needs a new flyer

Looking for a fresh and modern flyer design for a company called "Quillmarsh Fresh Co". We provide healthy and delicious meals to families, business offices and health care workers. We would like to see designs that communicate freshness, convenience, non contact delivery and customizable meal plan options. We would like to see designs that mirror our website colors, look and feel: quillmarshfreshco.com

Target Market(s)

Families, Business Offices, Health care workers

Requirements
Must have
• Color scheme and layout matching our brand and website
Our Logo
Modern clean/professional look
contact info: website, phone number, social media
Appropriate photos
Nice to have
• "How it Works" Summary

```html
<!DOCTYPE html>
<html lang="en">
<head>
<meta charset="utf-8">
<title>Quillmarsh Fresh Co – Meal Delivery Flyer</title>
<link rel="stylesheet" href="https://fonts.googleapis.com/css2?family=Roboto+Condensed:wght@300;400;700&family=Raleway:wght@200&display=swap">
<style>
  :root {
    --bg: #e9e9eb;
    --paper: #ffffff;
    --forest: #1f4d24;
    --forest-deep: #143a18;
    --green: #1a9a2c;
    --green-bright: #1fba35;
    --green-lime: #8fd14f;
    --ink: #1b1b1b;
    --footer: #22262a;
    --white: #ffffff;
  }
  * { box-sizing: border-box; margin: 0; padding: 0; }
  html, body { width: 1200px; height: 960px; overflow: hidden; }
  body { background: var(--bg); font-family: "Roboto Condensed", Arial, sans-serif; color: var(--ink); }

  .flyer {
    position: absolute; left: 280px; top: 27px; width: 640px; height: 905px;
    background: var(--paper); overflow: hidden;
    box-shadow: 0 6px 24px rgba(0,0,0,.18);
  }

  /* hero */
  .hero-photo {
    position: absolute; left: 0; top: 0; width: 640px; height: 400px;
    background:
      radial-gradient(ellipse at 70% 35%, #c84a2c 0%, rgba(200,74,44,0) 30%),
      radial-gradient(ellipse at 85% 15%, #e3b526 0%, rgba(227,181,38,0) 22%),
      radial-gradient(ellipse at 60% 70%, #5e9c3a 0%, rgba(94,156,58,0) 40%),
      linear-gradient(100deg, var(--forest-deep) 0%, var(--forest) 40%, #3f6b2e 70%, #6b8a3c 100%);
  }
  .brand {
    position: absolute; left: 46px; top: 120px; display: flex; align-items: center; gap: 10px;
    color: var(--white); font-weight: 700; font-size: 22px; letter-spacing: 1px; text-transform: uppercase;
  }
  .brand-dot { width: 16px; height: 16px; border-radius: 50%; background: var(--green-lime); }

  .contact { position: absolute; left: 46px; top: 220px; color: var(--white); }
  .contact-label { font-weight: 700; font-size: 20px; text-transform: uppercase; }
  .contact-phone { font-weight: 700; font-size: 26px; margin-bottom: 8px; }
  .contact-row { display: flex; align-items: center; gap: 8px; font-size: 13px; margin-top: 5px; }
  .contact-row svg { width: 16px; height: 16px; }
  .contact-rule { width: 220px; height: 1px; background: rgba(255,255,255,.6); margin: 10px 0 8px; }
  .service { font-size: 17px; font-weight: 700; text-transform: uppercase; }
  .service span { font-weight: 300; }
  .service-sub { font-size: 12px; font-weight: 700; color: var(--green-lime); text-transform: uppercase; }

  .headline {
    position: absolute; left: 330px; top: 205px; color: var(--white);
    font-family: "Raleway", Arial, sans-serif; font-weight: 200; font-size: 38px;
    line-height: 1.05; text-transform: uppercase; letter-spacing: 2px;
  }

  .family-illustration {
    position: absolute; right: 30px; top: 335px; width: 200px; height: 95px; border-radius: 6px;
    background: radial-gradient(ellipse at center, #f3c7a8 0%, #e8734f 45%, rgba(255,255,255,0) 75%);
  }

  /* intro */
  .intro { position: absolute; left: 40px; top: 438px; width: 560px; font-size: 12.5px; line-height: 1.35; }
  .intro-title { color: var(--green-bright); font-weight: 700; font-size: 17px; text-transform: uppercase; }

  .how-band {
    position: absolute; left: 30px; top: 522px; width: 580px; height: 36px;
    background: linear-gradient(90deg, var(--green-bright), var(--green));
    color: var(--white); display: flex; align-items: center; justify-content: center; gap: 10px;
    text-transform: uppercase;
  }
  .how-band strong { font-size: 20px; }
  .how-band small { font-size: 12px; font-weight: 700; }

  .plans-heading {
    position: absolute; left: 30px; top: 570px; width: 580px; display: flex; align-items: center; gap: 14px;
    font-weight: 700; font-size: 20px; text-transform: uppercase; white-space: nowrap;
  }
  .plans-heading::before, .plans-heading::after { content: ""; flex: 1; height: 1px; background: var(--green); }

  .plans { position: absolute; left: 30px; top: 608px; width: 580px; display: flex; gap: 10px; }
  .plan { flex: 1; height: 205px; background: linear-gradient(160deg, var(--green-bright), var(--green)); color: var(--white); padding: 12px; text-align: center; }
  .plan-name { background: var(--white); color: var(--green); font-weight: 700; font-size: 22px; text-transform: uppercase; padding: 2px 0; }
  .plan-price { display: flex; align-items: flex-end; justify-content: center; gap: 4px; margin: 10px 0 8px; }
  .plan-price b { font-size: 36px; font-weight: 400; line-height: 1; }
  .plan-price span { font-size: 10px; text-align: left; text-transform: uppercase; line-height: 1.2; white-space: nowrap; }
  .plan-desc { font-size: 10.5px; text-transform: uppercase; line-height: 1.3; margin-bottom: 10px; }
  .plan-extra { font-size: 10.5px; line-height: 1.3; }
  .plan-extra em { display: block; font-style: normal; text-transform: uppercase; margin-bottom: 3px; }

  .tagline { position: absolute; left: 30px; top: 826px; width: 580px; display: flex; align-items: center; justify-content: space-between; }
  .tagline p { font-weight: 700; font-size: 19px; text-transform: uppercase; }
  .socials { display: flex; gap: 6px; }
  .socials i { width: 20px; height: 20px; border-radius: 50%; background: var(--forest); display: block; }

  .footer {
    position: absolute; left: 0; bottom: 0; width: 640px; height: 42px; background: var(--footer);
    color: #c9ccd0; font-size: 9px; text-transform: uppercase; display: flex; align-items: center; justify-content: center; padding: 0 20px; text-align: center;
  }
</style>
</head>
<body>
<article class="flyer">
  <div class="hero-photo" role="img" aria-label="Photograph of fresh vegetables – peppers, tomatoes, cabbage, carrots and greens – on a dark green wooden table"></div>

  <div class="brand"><i class="brand-dot"></i>Quillmarsh Fresh Co</div>

  <div class="contact">
    <p class="contact-label">For order:</p>
    <p class="contact-phone">555-014-2290</p>
    <p class="contact-row"><svg viewBox="0 0 16 16"><circle cx="8" cy="8" r="8" fill="#8fd14f"/><path d="M5 4l2 2-1 1.2a6 6 0 0 0 2.8 2.8L10 9l2 2-1.3 1.3C7.8 12 4 8.2 3.7 5.3z" fill="#1f4d24"/></svg>hello@quillmarshfreshco.com</p>
    <p class="contact-row"><svg viewBox="0 0 16 16"><circle cx="8" cy="8" r="8" fill="#8fd14f"/><rect x="4" y="5" width="8" height="6" fill="none" stroke="#1f4d24"/><path d="M4 5l4 3 4-3" fill="none" stroke="#1f4d24"/></svg>www.quillmarshfreshco.com</p>
    <div class="contact-rule"></div>
    <p class="service">Home delivery <span>or</span> pick up</p>
    <p class="service-sub">At our preferred delivery locations</p>
  </div>

  <h1 class="headline">Fresh &amp; Fit<br>Meal Delivery</h1>

  <div class="family-illustration" role="img" aria-label="Illustration of a family sharing a meal at a table"></div>

  <section class="intro">
    <h2 class="intro-title">Quillmarsh Fresh Co</h2>
    <p>Fit and fresh prepared meals, paleo, gluten free and vegetarian options. Family inspired recipes that are fully cooked ready to eat, wholesome balanced meals, convenient to "grab and go" perfect for busy families and athletes with a schedule to keep.</p>
  </section>

  <div class="how-band"><strong>How it works -</strong><small>In three simple steps</small></div>

  <h2 class="plans-heading">Find the plan that fits you</h2>

  <section class="plans">
    <div class="plan">
      <h3 class="plan-name">Four Fresh</h3>
      <div class="plan-price"><b>$55</b><span>+$10 for portion plus<br>/week</span></div>
      <p class="plan-desc">Our most popular subscription! Four meals a week made fresh locally!</p>
      <p class="plan-extra"><em>Portion plus</em>Includes 50% more food per meals! Only $10 more!</p>
    </div>
    <div class="plan">
      <h3 class="plan-name">Eight Fresh</h3>
      <div class="plan-price"><b>$99</b><span>+$20 for portion plus<br>/week</span></div>
      <p class="plan-desc">Love the taste of Quillmarsh Fresh Co? Get more with our eight meal plan.</p>
      <p class="plan-extra"><em>Portion plus</em>Includes 50% more food per meals! Only $20 more!</p>
    </div>
    <div class="plan">
      <h3 class="plan-name">16 Meals</h3>
      <div class="plan-price"><b>$160</b><span>Couples plan<br>+$35 for portion plus<br>/week</span></div>
      <p class="plan-desc">Two people? Whole family? Get sixteen meals a week with our couple's plan.</p>
      <p class="plan-extra"><em>Portion plus</em>Includes 50% more food per meals! Only $35 more!</p>
    </div>
  </section>

  <div class="tagline">
    <p>We provide fresh, fully cooked, ready to eat meals!</p>
    <div class="socials"><i></i><i></i><i></i></div>
  </div>

  <footer class="footer">Please place your order by midnight on Saturday for that week's deliveries, any orders received after that will go on the following week order.</footer>
</article>
</body>
</html>
```